Design a Small Graphic for a client brochure and Website

We need a a fairly simple diagram/graphic to replace the existing graphic in our brochures and website. We are a Private Wealth Advice firm, dealing with high-end clients. We would like to be able to copyright the final design. We need this design to be stylish and have a long shelf-life.
The original design is quite old and was not updated to reflect our company growth or changes in our website design and brochure designs.
Updates

Target Market(s)

Private Wealth clients
High end
Age 45 plus

Industry/Entity Type

Finance

Font styles to use
Sans Serif
Other font styles liked:
• Stag Sans

Requirements
Must have
• Corporate colours only - plus white
• Pantone 288c (Blue)
• Pantone Cool grey 10c
• Pantone 666c (purple - only limited use for highlighting etc)
• Corporate fonts only
• Stag Sans light, book and thin
• Must provide AI editable files
• Must be able to scale to size and remove/replace any text
• Must be in keeping with our brochures and website which can be viewed at www.ridgefold-advisory.com.au
Nice to have
• We want something more vibrant than the image we are using. Something which is in keeping with our image but that is really eye catching.

```html
<!DOCTYPE html>
<html lang="en">
<head>
<meta charset="utf-8">
<title>Relationship Management – Ridgefold Partners</title>
<link rel="stylesheet" href="https://fonts.googleapis.com/css2?family=Roboto:wght@300;400;700&display=swap">
<style>
  :root {
    --backdrop: #e6e7ea;
    --paper: #ffffff;
    --frame: #8a8c92;
    --blue-288: #054283;
    --navy: #1e2a5a;
    --blue-light: #3563ae;
    --title-blue: #0a3585;
    --cool-grey: #4a4e5a;
    --purple-666: #a99bcb;
    --ink: #1a1a1a;
  }
  html, body {
    margin: 0;
    width: 1200px;
    height: 1200px;
    overflow: hidden;
    background: var(--backdrop);
  }
  .sheet {
    position: absolute;
    left: 200px;
    top: 33px;
    width: 800px;
    height: 1133px;
    background: var(--paper);
    box-shadow: 0 2px 10px rgba(0,0,0,0.12);
  }
  .sheet svg { display: block; width: 100%; height: 100%; }
  .type { font-family: "Roboto", Arial, sans-serif; }
  .segment-label { fill: #ffffff; font-size: 18px; font-weight: 300; text-anchor: middle; }
  .diagram-title { fill: var(--title-blue); font-size: 27px; font-weight: 300; text-anchor: middle; }
  .brand-name { fill: var(--navy); font-size: 24px; font-weight: 400; text-anchor: end; }
  .swatch-label { fill: var(--ink); font-size: 5px; font-weight: 700; }
</style>
</head>
<body>
  <main class="sheet">
    <svg viewBox="0 0 696 986" class="type" role="img" aria-label="Relationship Management diagram">
      <rect class="page-frame" x="23" y="26" width="649" height="937" fill="none" stroke="var(--frame)" stroke-width="1"/>

      <!-- brand -->
      <text class="brand-name" x="645" y="118">Ridgefold Partners</text>

      <!-- four-part pie chart -->
      <g class="pie-chart">
        <circle cx="348" cy="474" r="237" fill="var(--blue-288)"/>

        <path class="segment" fill="var(--blue-light)" d="M342,468 L140,468 A208,208 0 0 1 342,266 Z"/>
        <path class="segment" fill="var(--navy)" d="M354,468 L354,266 A208,208 0 0 1 556,468 Z"/>
        <path class="segment" fill="var(--blue-light)" d="M354,480 L556,480 A208,208 0 0 1 354,682 Z"/>
        <path class="segment" fill="var(--navy)" d="M342,480 L342,682 A208,208 0 0 1 140,480 Z"/>

        <circle class="hub" cx="348" cy="474" r="14" fill="#ffffff"/>

        <text class="segment-label" x="262" y="404">Purpose</text>
        <text class="segment-label" x="434" y="404">Investment</text>
        <text class="segment-label" x="434" y="426">Consulting</text>
        <text class="segment-label" x="262" y="550">Wealth</text>
        <text class="segment-label" x="262" y="573">Planning</text>
        <text class="segment-label" x="434" y="550">Your</text>
        <text class="segment-label" x="434" y="573">Legacy</text>
      </g>

      <text class="diagram-title" x="348" y="766">Relationship Management</text>

      <!-- colour key -->
      <g class="colour-key">
        <rect x="39" y="926" width="22" height="22" fill="var(--cool-grey)"/>
        <text class="swatch-label" x="70" y="936">Cool Gray 10C</text>
        <text class="swatch-label" x="70" y="942">CMYK 40 30 20 66</text>

        <rect x="133" y="926" width="22" height="22" fill="var(--blue-288)"/>
        <text class="swatch-label" x="164" y="936">Pantone 288c (Blue)</text>
        <text class="swatch-label" x="164" y="942">CMYK 100 75 6 34</text>

        <rect x="230" y="926" width="22" height="22" fill="var(--purple-666)"/>
        <text class="swatch-label" x="261" y="936">Pantone 666c</text>
        <text class="swatch-label" x="261" y="942">CMYK 36 39 3 5</text>
      </g>
    </svg>
  </main>
</body>
</html>
```